Lantern Sisters Ministries Logo/Business Card

Lantern Sisters are women full of God’s love and restorative grace, who have the desire to lead other women to embrace the beautiful creation that God intended them to be. Lantern Sisters walk together with other women alongside of God toward a life of healing, restoration and empowerment… through mentoring, spiritual guidance, temporary shelter, comprehensive care, and connections to a longer-term plan that leads to renewal and wholeness in Christ.

Lantern Sisters Ministries is an organization that embraces women and children whose lives have been affected by human trafficking, prison, foster care, homelessness, addictions, and other circumstances that prevent them from achieving their full potential in Christ Jesus. We believe that God has a unique plan and purpose for every individual. Through God’s transformational power and relationships with counselors, mentors, and others, anyone can break free from the chains and bondage of slavery, addictions and the strongholds of life.

We are just starting to brand our organization, and need both business cards and a logo. We do not have a logo yet, and would like design ideas. One of our young ladies (rescued from trafficking) has a vision of a logo with a crown with 3 ladies below/around it (representing healing, restoration, empowerment). Another lady has an idea of blending a crown, heart, and cross into the logo. We are open to creative suggestions.

Target Market(s)

Donations from churches, businesses, organizations and individuals with a passion for Trafficking and Justice

Industry/Entity Type

Business

Contact Information for Business Card

Lantern Sisters Ministries
women walking together toward healing, restoration and empowerment (tag line - italics)

Card 1:
Marla Tibbets, Director
555.203.7718
marla@lanternsistersministries.example
www.lanternsistersministries.example (optional)

Card 2:
Rosalind Pickett, Director
555.617.4420
ros@lanternsistersministries.example

```html
<!DOCTYPE html>
<html lang="en">
<head>
<meta charset="utf-8">
<title>Lantern Sisters Ministries – Business Card</title>
<link rel="stylesheet" href="https://fonts.googleapis.com/css2?family=Tinos:ital@0;1&display=swap">
<style>
  :root {
    --paper: #ffffff;
    --ink: #111111;
    --accent-red: #c1202f;
    --cross-red: #c02030;
    --cross-lilac: #a688c4;
    --art-tone: #e4e4e4;
    --serif: "Tinos", "Times New Roman", serif;
  }
  html, body {
    margin: 0;
    padding: 0;
    width: 1200px;
    height: 724px;
    overflow: hidden;
    background: var(--paper);
  }
  p { margin: 0; }
  .card {
    position: relative;
    width: 1200px;
    height: 724px;
    box-sizing: border-box;
    border: 2px solid var(--ink);
    background: var(--paper);
    font-family: var(--serif);
    color: var(--ink);
    overflow: hidden;
  }
  .cross {
    position: absolute;
    left: 0;
    top: 0;
  }
  .logo-box {
    position: absolute;
    left: 0;
    top: 0;
    width: 448px;
    height: 431px;
    box-sizing: border-box;
    border: 4px solid var(--ink);
    background: var(--paper);
    display: flex;
    flex-direction: column;
    justify-content: center;
    padding: 0 30px 0 44px;
  }
  .brand-line {
    font-size: 64px;
    line-height: 1.08;
  }
  .brand-line:nth-child(2) { padding-left: 40px; }
  .brand-line:nth-child(3) { padding-left: 80px; }
  .tagline {
    margin-top: 22px;
    font-size: 20px;
    font-style: italic;
    line-height: 1.3;
  }
  .contact {
    position: absolute;
    left: 463px;
    line-height: 1;
    white-space: nowrap;
  }
  .contact.name { top: 76px; font-size: 37px; }
  .contact.phone { top: 172px; font-size: 37px; }
  .contact.email { top: 362px; font-size: 20px; }
  .prayer-art {
    position: absolute;
    left: 991px;
    top: 22px;
    width: 179px;
    height: 200px;
    box-sizing: border-box;
    border: 2px solid #555;
    background: linear-gradient(180deg, #f4f4f4, var(--art-tone));
  }
  .pillar {
    position: absolute;
    color: var(--accent-red);
    white-space: nowrap;
    line-height: 1;
  }
  .pillar.healing { left: 90px; top: 450px; font-size: 53px; }
  .pillar.restoration { left: 246px; top: 516px; font-size: 48px; }
  .pillar.empowerment { left: 449px; top: 585px; font-size: 44px; }
  .web {
    position: absolute;
    left: 43px;
    top: 638px;
    font-size: 39px;
    line-height: 1;
    white-space: nowrap;
  }
</style>
</head>
<body>
  <div class="card">
    <svg class="cross" width="1200" height="724" viewBox="0 0 1200 724" aria-hidden="true">
      <rect x="448" y="230" width="752" height="108" fill="var(--cross-lilac)"/>
      <rect x="836" y="0" width="103" height="638" fill="var(--cross-lilac)"/>
      <rect x="448" y="267" width="752" height="35" fill="var(--cross-red)"/>
      <rect x="868" y="0" width="37" height="638" fill="var(--cross-red)"/>
    </svg>

    <div class="logo-box">
      <span class="brand-line">Lantern</span>
      <span class="brand-line">Sisters</span>
      <span class="brand-line">Ministries</span>
      <p class="tagline">women walking together toward healing, restoration and empowerment</p>
    </div>

    <p class="contact name">Marla Tibbets, Director</p>
    <p class="contact phone">Phone: (555) 203-7718</p>
    <p class="contact email">marla@lanternsistersministries.example</p>

    <div class="prayer-art" role="img" aria-label="Illustration of hands folded in prayer"></div>

    <p class="pillar healing">Healing</p>
    <p class="pillar restoration">Restoration</p>
    <p class="pillar empowerment">Empowerment</p>

    <p class="web">Web:www.lanternsistersministries.example</p>
  </div>
</body>
</html>
```